Investment Fund Investor newsletter

I deleted the tear sheet example which was provided for design purposes only and not for content. Please see the simple outline for the newsletter and the related sections.

Please be clear this project is for a newsletter template. This means a template that can be updated on a monthly or quarterly basis with new content for our audience. Sections should include: Operations Update, Financial Update, Energy Investor News.

We need a template for a newsletter that can be sent out in Word format and also able to send out via Mailchimp. Audience are current investors in our oil and gas fund. These investors are high net worth individuals and private equity firms so the branding needs to be high end, sophisticated and corporate. Please see website and attached tear sheet for the type of branding that we want to match. Website is www.quarrybell-power.com
Please see website and tear sheet for the color scheme that we want.

Target Market(s)

Our current fund investors that include high net worth investors and CEOs of private equity companies

Industry/Entity Type

oil and gas... investment

Font styles to use
Serif

Requirements
Must have
• Word file and can send via Mailchimp too

```html
<!DOCTYPE html>
<html lang="en">
<head>
<meta charset="utf-8">
<title>Quarrybell Power Partners – Investor Newsletter</title>
<link rel="stylesheet" href="https://fonts.googleapis.com/css2?family=Noto+Serif:wght@400;500&family=Roboto:wght@300;400;500&display=swap">
<style>
  :root {
    --accent: #1a9fe3;
    --band: #1c9be2;
    --ink: #111111;
    --body: #7d7d7d;
    --muted: #666666;
    --white: #ffffff;
    --footer: #0b0b0c;
    --serif: "Noto Serif", Georgia, serif;
    --sans: "Roboto", Arial, sans-serif;
  }
  * { box-sizing: border-box; margin: 0; padding: 0; }
  html, body { width: 1200px; height: 4286px; overflow: hidden; background: var(--white); }
  body { font-family: var(--sans); color: var(--body); position: relative; }
  .abs { position: absolute; }

  /* Header */
  .header { position: absolute; top: 0; left: 0; width: 1200px; height: 150px; background: var(--white); }
  .brand { position: absolute; left: 150px; top: 40px; font-family: var(--serif); color: var(--ink); font-weight: 500; text-align: center; line-height: 1.1; }
  .brand .name { font-size: 27px; letter-spacing: 3px; display: block; }
  .brand .sub { font-size: 11px; letter-spacing: 5px; display: block; }
  .call-icon { position: absolute; left: 521px; top: 35px; width: 80px; height: 80px; border-radius: 50%; background: var(--white); box-shadow: 0 4px 18px rgba(0,0,0,.12); display: flex; align-items: center; justify-content: center; }
  .call-text { position: absolute; left: 639px; top: 38px; color: var(--ink); }
  .call-text .label { font-size: 19px; color: var(--muted); display: block; }
  .call-text .num { font-size: 26px; font-weight: 500; display: block; margin-top: 12px; }
  .social { position: absolute; display: flex; gap: 8px; }
  .social span { width: 50px; height: 50px; border-radius: 50%; background: var(--accent); display: block; }
  .header .social { left: 882px; top: 50px; }

  /* Hero */
  .hero { position: absolute; top: 150px; left: 0; width: 1200px; height: 599px;
    background: linear-gradient(180deg, #1b3f8c 0%, #3d5fa6 28%, #c76a4a 55%, #f08a1e 72%, #d2450e 86%, #1a0c08 100%); }
  .hero-box { position: absolute; left: 265px; top: 178px; width: 670px; height: 243px; background: rgba(255,255,255,.88);
    display: flex; align-items: center; justify-content: center; text-align: center;
    font-family: var(--serif); font-size: 30px; line-height: 48px; color: var(--ink); }
  .hl { color: var(--accent); }

  /* Update sections */
  .title { font-family: var(--serif); font-weight: 400; font-size: 33px; color: var(--ink); }
  .copy { font-size: 21px; line-height: 39px; color: var(--body); font-weight: 300; }
  .hex { position: absolute; width: 383px; height: 439px;
    clip-path: polygon(50% 0, 100% 25%, 100% 75%, 50% 100%, 0 75%, 0 25%); }
  .hex-rig { background: linear-gradient(160deg, #8fa7e6 0%, #c9cfe8 40%, #5a5a5e 70%, #2a2a2c 100%); }
  .hex-pipes { background: linear-gradient(135deg, #3a2a1c 0%, #8a5a2e 35%, #c98a45 55%, #5a3f26 80%, #2a1e14 100%); }
  .hex-jack { background: linear-gradient(180deg, #2c47b8 0%, #5878d6 40%, #a7b0d8 62%, #e0a060 75%, #050505 88%); }

  /* Who we are */
  .band { position: absolute; top: 2313px; left: 0; width: 1200px; height: 496px;
    background: linear-gradient(180deg, #1f9de4 0%, #1c9be2 60%, #2aa3e0 80%, #3aa8d8 100%); }
  .band-photo { position: absolute; left: 0; top: 0; width: 1200px; height: 496px;
    background: linear-gradient(180deg, rgba(255,255,255,0) 55%, rgba(120,190,220,.35) 80%, rgba(60,150,200,.4) 100%); }
  .band h2 { position: absolute; left: 602px; top: 90px; font-family: var(--serif); font-weight: 500; font-size: 46px; color: var(--white); letter-spacing: .5px; }
  .band p { position: absolute; left: 602px; top: 172px; width: 448px; font-size: 21.5px; line-height: 39px; color: var(--white); text-align: justify; }

  /* Strategy */
  .strategy-title { position: absolute; top: 2905px; left: 0; width: 1200px; text-align: center; font-family: var(--serif); font-size: 40px; color: var(--ink); }
  .strategy-intro { position: absolute; top: 2986px; left: 150px; width: 900px; text-align: center; }
  .strategy-left { position: absolute; top: 3252px; left: 150px; width: 452px; text-align: justify; }
  .bullets { position: absolute; top: 3466px; left: 150px; width: 452px; list-style: none; }
  .bullets li { position: relative; padding-left: 49px; margin-bottom: 11px; }
  .bullets svg { position: absolute; left: 0; top: 10px; }
  .strategy-photo { position: absolute; left: 669px; top: 3190px; width: 381px; height: 554px;
    background: radial-gradient(circle at 50% 62%, #fff6c0 0%, #ffd23a 22%, #f3a51a 55%, #b8600c 85%, #5a2a06 100%); }

  /* Footer */
  .footer { position: absolute; top: 3857px; left: 0; width: 1200px; height: 429px; background: var(--footer); color: var(--white); }
  .footer .brand { left: 0; width: 1200px; top: 60px; color: var(--white); }
  .footer-line { position: absolute; left: 0; width: 1200px; display: flex; justify-content: center; align-items: center; gap: 14px; font-size: 20px; }
  .footer-line .sep { margin: 0 16px; }
  .footer .social { left: 525px; top: 276px; gap: 5px; }
  .footer .social span { width: 46px; height: 46px; }
  .rule { position: absolute; left: 150px; top: 348px; width: 900px; height: 1px; background: #3a3a3a; }
  .copyright { position: absolute; top: 370px; left: 0; width: 1200px; text-align: center; font-size: 18px; }
</style>
</head>
<body>

<header class="header">
  <div class="brand"><span class="name">QUARRYBELL</span><span class="sub">POWER PARTNERS</span></div>
  <div class="call-icon">
    <svg width="30" height="30" viewBox="0 0 24 24"><path fill="#1a9fe3" d="M6.6 10.8a15.1 15.1 0 0 0 6.6 6.6l2.2-2.2a1 1 0 0 1 1-.25 11.4 11.4 0 0 0 3.6.57 1 1 0 0 1 1 1V20a1 1 0 0 1-1 1A17 17 0 0 1 3 4a1 1 0 0 1 1-1h3.5a1 1 0 0 1 1 1c0 1.25.2 2.45.57 3.57a1 1 0 0 1-.25 1z"/></svg>
  </div>
  <div class="call-text"><span class="label">CALL US:</span><span class="num">(432) 555-0187</span></div>
  <div class="social"><span></span><span></span><span></span></div>
</header>

<section class="hero" role="img" aria-label="Oil pump jacks silhouetted against an orange sunset sky">
  <div class="hero-box">
    <div>CONSOLIDATING WEST TEXAS<br>CONVENTIONAL <span class="hl">OIL &amp; GAS ASSETS</span><br>INTO A HIGH RETURN FUND</div>
  </div>
</section>

<!-- Operations update -->
<h2 class="title abs" style="left:150px;top:902px;">OPERATIONS <span class="hl">UPDATE</span></h2>
<p class="copy abs" style="left:150px;top:983px;width:452px;">Lorem ipsum dolor sit amet, consectetur adip isc ing elit, sed do eiusmod tempor incididunt ut lab ore et dolore magna aliqu nim ad minim veniam, quis nostrud exercitationat. Sed do eiusmod tem por incididunt ut lab ore et dolore magna aliqua. Ut enim ad minim veniamea.</p>
<div class="hex hex-rig" style="left:669px;top:842px;" role="img" aria-label="Drilling rig beside a stack of steel pipes under a blue sky"></div>

<!-- Financial update -->
<div class="hex hex-pipes" style="left:150px;top:1311px;" role="img" aria-label="Close view of rusty oilfield pipes"></div>
<h2 class="title abs" style="left:597px;top:1371px;">FINANCIAL <span class="hl">UPDATE</span></h2>
<p class="copy abs" style="left:597px;top:1452px;width:453px;">Lorem ipsum dolor sit amet, consectetur adip isc ing elit, sed do eiusmod tempor incididunt ut lab ore et dolore magna aliqu nim ad minim veniam, quis nostrud exercitationat. Sed do eiusmod tem por incididunt ut lab ore et dolore magna aliqua. Ut enim ad minim veniamea.</p>

<!-- Energy investor news -->
<h2 class="title abs" style="left:150px;top:1841px;">ENERGY <span class="hl">INVESTOR NEWS</span></h2>
<p class="copy abs" style="left:150px;top:1921px;width:452px;">Lorem ipsum dolor sit amet, consectetur adip isc ing elit, sed do eiusmod tempor incididunt ut lab ore et dolore magna aliqu nim ad minim veniam, quis nostrud exercitationat. Sed do eiusmod tem por incididunt ut lab ore et dolore magna aliqua. Ut enim ad minim veniamea.</p>
<div class="hex hex-jack" style="left:669px;top:1779px;" role="img" aria-label="Pump jack silhouette against a blue evening sky"></div>

<!-- Who we are -->
<section class="band">
  <div class="band-photo" role="img" aria-label="Oilfield with pump jacks under a blue tint"></div>
  <h2>WHO WE ARE</h2>
  <p>We are a diverse team of professionals with over 100 years of combined experience in oil and gas. We are uniquely positioned to take advantage of opportunities in the conventional oil and gas space and are fully supported by the dedicated operating experience of Harlan Ridge Resources.</p>
</section>

<!-- Focused strategy -->
<h2 class="strategy-title">FOCUSED <span class="hl">STRATEGY</span></h2>
<p class="copy strategy-intro">We believe there is still enormous opportunity in the many attractive conventional assets in West Texas. But it takes the right experience and team to make it happen. We have that experience and we have that team. Our aim is to acquire, optimize and operate West Texas conventional oil and gas assets to provide attractive returns to our investors.</p>
<p class="copy strategy-left">Many of these assets, while still very productive or possessing good behind the pipe potential, may not fit the strategy of their current owners. By working with owners of these kinds of assets, we help them:</p>
<ul class="copy bullets">
  <li><svg width="19" height="19" viewBox="0 0 20 20"><circle cx="10" cy="10" r="10" fill="#1a9fe3"/><path d="M6 10h7M10 6.5l3.5 3.5-3.5 3.5" stroke="#fff" stroke-width="2" fill="none"/></svg>Free up capital and energy</li>
  <li><svg width="19" height="19" viewBox="0 0 20 20"><circle cx="10" cy="10" r="10" fill="#1a9fe3"/><path d="M6 10h7M10 6.5l3.5 3.5-3.5 3.5" stroke="#fff" stroke-width="2" fill="none"/></svg>Keep focused on the most strategic parts of their oil and gas portfolios</li>
  <li><svg width="19" height="19" viewBox="0 0 20 20"><circle cx="10" cy="10" r="10" fill="#1a9fe3"/><path d="M6 10h7M10 6.5l3.5 3.5-3.5 3.5" stroke="#fff" stroke-width="2" fill="none"/></svg>Rest assured that any assets divested will be in the hands of an experienced operator</li>
</ul>
<div class="strategy-photo" role="img" aria-label="Pump jack silhouetted against a bright golden sunset"></div>

<!-- Footer -->
<footer class="footer">
  <div class="brand"><span class="name">QUARRYBELL</span><span class="sub">POWER PARTNERS</span></div>
  <div class="footer-line" style="top:185px;">
    <svg width="14" height="20" viewBox="0 0 14 20"><path fill="#1a9fe3" d="M7 0a7 7 0 0 0-7 7c0 5 7 13 7 13s7-8 7-13a7 7 0 0 0-7-7zm0 9.5A2.5 2.5 0 1 1 7 4.5a2.5 2.5 0 0 1 0 5z"/></svg>
    <span>1200 W. Wall Street, Suite 210 Midland,</span><span class="sep">|</span>
    <svg width="18" height="18" viewBox="0 0 24 24"><path fill="#1a9fe3" d="M6.6 10.8a15.1 15.1 0 0 0 6.6 6.6l2.2-2.2a1 1 0 0 1 1-.25 11.4 11.4 0 0 0 3.6.57 1 1 0 0 1 1 1V20a1 1 0 0 1-1 1A17 17 0 0 1 3 4a1 1 0 0 1 1-1h3.5a1 1 0 0 1 1 1c0 1.25.2 2.45.57 3.57a1 1 0 0 1-.25 1z"/></svg>
    <span>(432) 555-0187</span>
  </div>
  <div class="footer-line" style="top:232px;">
    <svg width="20" height="15" viewBox="0 0 20 15"><rect width="20" height="15" rx="2" fill="#1a9fe3"/><path d="M1 1l9 7 9-7" stroke="#0b0b0c" stroke-width="1.6" fill="none"/></svg>
    <span>info@quarrybell-power.com</span><span class="sep">|</span>
    <svg width="18" height="18" viewBox="0 0 20 20"><circle cx="10" cy="10" r="9" fill="#1a9fe3"/><path d="M1 10h18M10 1c3 3 3 15 0 18M10 1c-3 3-3 15 0 18" stroke="#0b0b0c" stroke-width="1.2" fill="none"/></svg>
    <span>www.quarrybell-power.com</span>
  </div>
  <div class="social"><span></span><span></span><span></span></div>
  <div class="rule"></div>
  <div class="copyright">© 2022 QUARRYBELL &nbsp;/&nbsp; All Rights Reserved</div>
</footer>

</body>
</html>
```